Etikett für Rotweinflasche
Liebe pinselhaus Studio, wir werden uns bei der endgültigen Etikettengestaltung (finale Größe + Rückseite) noch an Euch melden. Bitte sendet uns euren Kontakt an marta.lindner@montelvo.wine
Zielgruppe
Montelvo Italia ist ein exklusives Boutique-Weingut in Sizilien, das hochqualitative Spitzenweine in kleinen Mengen mit modernster Technologie und stets nachhaltig erzeugt. Wir hinterfragen sowohl in der Agronomie im Weingarten als auch in der Önologie im Weinkeller alle herrschenden Traditionen und trachten danach, stets das beste Endprodukt zu kreieren. Der vulkanische, kalkreiche Boden Siziliens sowie trockene, sonnenreiche und niederschlagsarme Vegetationsperioden sind unsere optimale Basis.
Zielgruppe: Internationale Genussmenschen jeglichen Alters, die sich bewusst auch höherpreisige Weine (um die €30+) gönnen , vor allem kunstaffine young professionals mit Qualitäts-& Nachhaltigkeitsanspruch
Aufgabenstellung
Das Etikett ist für Rotwein-Flaschen (Cabernet Sauvignon / Nero D'Avola / Frappato / Syrah / Cerasuolo / Petit Verdot / sowie einen Bourdeaux-Cuveè aus Cabernet Sauvignon und Petit Verdot) .
Die Flasche ist reinschwarz, sehr hochwertig und schwer.
Flaschenform: Bordeauxflasche siehe technisches Datenblatt
Sleeve über dem Korken: schwarz mit weißer Schrift wie bisher
Zu gestalten ist das Etikett der Vorderseite. Zumindest die jeweilige Rotwein-Sorte ist auch textlich darzustellen (zwecks Scannen mit Traubly-App)
Der Kreativität kann freien Lauf gelassen werden! Unterscheidbarkeit vom Markt ist explizit gewollt.
Unsere aktuellen Etiketten und Markenauftritt siehe: https://montelvo.wine/shop/

```html
<!DOCTYPE html>
<html lang="de">
<head>
<meta charset="utf-8">
<title>Etikett Cabernet Sauvignon</title>
<link rel="stylesheet" href="https://fonts.googleapis.com/css2?family=Cormorant+Garamond:wght@500&display=swap">
<style>
  :root {
    --backdrop: #45474d;
    --backdrop-edge: #2b2c31;
    --label-green-deep: #1d4038;
    --label-green: #4d7f70;
    --label-mist: #8fb3a4;
    --label-peach: #efc2ae;
    --label-blush: #e6a897;
    --label-skin: #d49378;
    --label-hair: #c9a37e;
    --label-shadow: #101a18;
    --label-text: #f6f1ea;
  }
  html, body {
    margin: 0;
    padding: 0;
    width: 1200px;
    height: 900px;
    overflow: hidden;
  }
  .canvas {
    position: relative;
    width: 1200px;
    height: 900px;
    background: radial-gradient(ellipse at 50% 38%, var(--backdrop) 0%, var(--backdrop-edge) 100%);
  }
  .wine-label {
    position: absolute;
    left: 380px;
    top: 160px;
    width: 440px;
    height: 580px;
    overflow: hidden;
    box-shadow: 0 20px 44px rgba(0, 0, 0, 0.4);
  }
  .label-artwork {
    position: absolute;
    inset: 0;
    background:
      radial-gradient(ellipse 38% 22% at 70% 8%, rgba(239, 194, 174, 0.95) 0%, rgba(239, 194, 174, 0) 80%),
      radial-gradient(ellipse 30% 40% at 96% 22%, rgba(230, 168, 151, 0.85) 0%, rgba(230, 168, 151, 0) 80%),
      radial-gradient(ellipse 34% 16% at 40% 26%, rgba(201, 163, 126, 0.9) 0%, rgba(201, 163, 126, 0) 80%),
      radial-gradient(ellipse 16% 14% at 12% 30%, rgba(212, 147, 120, 0.9) 0%, rgba(212, 147, 120, 0) 80%),
      radial-gradient(ellipse 42% 13% at 52% 44%, rgba(228, 170, 140, 0.95) 0%, rgba(228, 170, 140, 0) 85%),
      radial-gradient(ellipse 22% 10% at 68% 52%, rgba(40, 32, 28, 0.75) 0%, rgba(40, 32, 28, 0) 85%),
      radial-gradient(ellipse 30% 18% at 42% 66%, rgba(212, 147, 120, 0.85) 0%, rgba(212, 147, 120, 0) 80%),
      radial-gradient(ellipse 24% 16% at 18% 88%, rgba(232, 170, 145, 0.9) 0%, rgba(232, 170, 145, 0) 80%),
      radial-gradient(ellipse 30% 26% at 14% 58%, rgba(143, 179, 164, 0.7) 0%, rgba(143, 179, 164, 0) 80%),
      radial-gradient(ellipse 50% 38% at 88% 86%, var(--label-shadow) 0%, rgba(16, 26, 24, 0) 80%),
      radial-gradient(ellipse 40% 30% at 82% 60%, rgba(77, 127, 112, 0.9) 0%, rgba(77, 127, 112, 0) 80%),
      linear-gradient(170deg, var(--label-mist) 0%, var(--label-green) 35%, var(--label-green-deep) 75%, var(--label-shadow) 100%);
  }
  .label-vignette {
    position: absolute;
    inset: 0;
    background: radial-gradient(ellipse 80% 75% at 50% 45%, rgba(0, 0, 0, 0) 60%, rgba(0, 0, 0, 0.35) 100%);
    pointer-events: none;
  }
  .varietal-name {
    position: absolute;
    top: 26px;
    left: 0;
    right: 0;
    margin: 0;
    text-align: center;
    font-family: "Cormorant Garamond", serif;
    font-weight: 500;
    font-size: 27px;
    line-height: 1;
    letter-spacing: 0.03em;
    color: var(--label-text);
    text-transform: uppercase;
    white-space: nowrap;
  }
</style>
</head>
<body>
  <main class="canvas">
    <section class="wine-label">
      <div class="label-artwork" role="img" aria-label="Malerische Szene eines sich küssenden Paares vor grünem Hintergrund mit Pfirsich- und Rosétönen"></div>
      <div class="label-vignette"></div>
      <h1 class="varietal-name">Cabernet Sauvignon</h1>
    </section>
  </main>
</body>
</html>
```